Mortgage Company Website / based from Lurent design

Mortgage company needs a WordPress site designed and developed using Pixel Harbor's Lurent framework. Existing site is BrellaMortgage.example.

Goals of website:
1) Attract new leads for Home loans (first-time home buyers, people moving to Dallas, and people re-financing their homes.
2) Attract and recruit new Loan Officers.

LOAN PRODUCTS OFFERED
Conventional
Jumbo
VA
FHA
USDA
Refinance
Construction Loans - not a main product. Don't like to do these.
Remodel

Target Market(s)

Middle to upper income families in the Dallas area.

Industry/Entity Type

Mortgage Brokerage

Coding

Coded - Design and coding required

Number of Pages Required

2 page

Requirements
Must have
• Must use one of the Lurent theme from Pixel Harbor for development
https://lurent.pixel-harbor.example/

Client is focused on higher-end clientele and likes the use of the color gold.

NAVIGATION
Home Loans
Mortgage Resources
About Us
Contact Us

Site must also look good on mobile phones and tablets. Lurent theme has breakpoints already developed so should make that easier.
Nice to have
• Client likes the designs of these sites:
https://crestmora.example/home-loans (this one was talked about as her favorite)
https://thependrickteam.example/
https://www.servicefirstloans.example/

- Overall wants the site to be clean with lots of white space

Wants to keep the imagery focused on the families and people buying the home.

Also likes the focus on giving back to the community from the example site provided. Brella gives to "Hands for Hounds"

Things that can be featured on the home page:
* Hero image on top
* Top of Q, Vantrell Market Leader award. Vantrell 100 Mortgage Market Leader 2020
* 3 Most recent blog posts
* Video from current homepage
* Get started form: Name, Email, Phone. Submit button
* Footer area can have navigation, contact info, and awards sections

some possible Lurent templates to choose from:
https://lurent.pixel-harbor.example/charity/
https://lurent.pixel-harbor.example/cryptocurrency/
https://lurent.pixel-harbor.example/freelancer/
https://lurent.pixel-harbor.example/finance/
https://lurent.pixel-harbor.example/financial-advisor/
https://lurent.pixel-harbor.example/university/
https://lurent.pixel-harbor.example/marketing-consultant/

```html
<!DOCTYPE html>
<html lang="en">
<head>
<meta charset="utf-8">
<title>Brella Mortgage – Home Page and Mobile</title>
<link href="https://fonts.googleapis.com/css2?family=Montserrat:wght@400;500;600;700&family=Questrial&display=swap" rel="stylesheet">
<style>
:root{
  --gold:#e3c54a;
  --ink:#2b2b2b;
  --grey:#707070;
  --line:#dedede;
  --soft:#f5f4f2;
  --panel:#fafafa;
  --dark:#3e3e3e;
  --stage:#efece8;
  --white:#ffffff;
}
*{margin:0;padding:0;box-sizing:border-box}
html,body{width:1200px;height:4455px;overflow:hidden;background:var(--white)}
body{position:relative;font-family:"Montserrat",sans-serif;color:var(--ink)}
.stage{position:absolute;left:0;top:0;width:1200px;height:623px;background:var(--stage)}
.stage-screen{position:absolute;left:294px;top:52px;width:565px;height:359px;overflow:hidden;background:var(--white);box-shadow:0 6px 24px rgba(0,0,0,.12)}
.stage-screen .hero-frame{transform:scale(1.197);transform-origin:0 0;width:472px;height:300px;position:relative}

.board-label{position:absolute;top:697px;font-family:"Questrial",sans-serif;font-size:34px;color:var(--ink)}
.label-desk{left:294px}
.label-mob{left:903px}

.thanks{position:absolute;left:104px;top:2838px;font-family:"Questrial",sans-serif;font-size:136px;line-height:172px;color:#111}

/* desktop page */
.desk{position:absolute;left:168px;top:761px;width:472px;height:1602px;background:var(--white);box-shadow:0 2px 10px rgba(0,0,0,.18);overflow:hidden}
.sec{position:relative;overflow:hidden}
.abs{position:absolute}
.brand{font-family:"Montserrat",sans-serif;font-weight:700;color:var(--ink);letter-spacing:.5px;display:flex;align-items:center;gap:3px}
.brand .dot{width:5px;height:5px;border-radius:50%;background:var(--gold)}
.btn{background:var(--gold);color:var(--ink);font-weight:600;display:flex;align-items:center;justify-content:center}
.photo{position:absolute}

.hero{height:287px;background:var(--panel)}
.hero .abs{z-index:2}
.hero .photo{z-index:1}
.hero .brand{left:29px;top:14px;font-size:13px}
.hero .phone{left:294px;top:15px;font-size:5.5px;color:var(--gold);display:flex;gap:2px;align-items:center}
.hero .login{left:367px;top:12px;width:60px;height:14px;font-size:5.5px}
.nav{left:207px;top:39px;display:flex;gap:15px;font-size:5.5px;color:var(--ink)}
.hero .kicker{left:29px;top:104px;font-size:6px;color:var(--grey);letter-spacing:.5px}
.hero .sub-kicker{left:29px;top:116px;font-size:14px;font-weight:600;color:var(--grey);letter-spacing:1px}
.hero .title{left:29px;top:134px;font-size:17px;font-weight:600;color:var(--ink);white-space:nowrap}
.hero .lede{left:29px;top:162px;width:168px;font-size:6.6px;line-height:10px;color:var(--ink)}
.hero .quote-btn{left:29px;top:195px;width:62px;height:13px;font-size:5.5px}
.hero .note{left:60px;top:214px;width:62px;height:22px;background:linear-gradient(135deg,#f1efe9,#e7e3da)}
.hero .hero-photo{left:226px;top:52px;width:246px;height:235px;background:radial-gradient(ellipse at 55% 45%,#d7a587 0%,#b68160 35%,#e6e2dc 72%,#f4f3f1 100%)}

.about{height:192px;background:linear-gradient(180deg,#f4f4f3,#ececeb)}
.about .video{left:29px;top:38px;width:203px;height:114px;background:linear-gradient(135deg,#f7f7f7,#d9d9d9)}
.play{position:absolute;left:50%;top:50%;width:22px;height:16px;margin:-8px 0 0 -11px;background:#222;border-radius:4px}
.play:after{content:"";position:absolute;left:8px;top:4px;border-left:7px solid #fff;border-top:4px solid transparent;border-bottom:4px solid transparent}
.h2{font-weight:500;color:var(--ink)}
.about .h2{left:240px;top:39px;font-size:11px}
.about .copy{left:240px;top:57px;width:190px;font-size:4.6px;line-height:7.6px;color:var(--grey)}
.about .more{left:240px;top:138px;width:58px;height:13px;font-size:5px}

.why{height:213px;background:var(--white)}
.why .why-photo{left:0;top:0;width:216px;height:213px;background:linear-gradient(120deg,#e8d4bd 0%,#c99a78 40%,#f1ebe3 100%)}
.why .h2{left:233px;top:27px;font-size:12px}
.why ul{left:233px;top:50px;list-style:none;font-size:5.3px;color:var(--ink)}
.why li{height:16.8px;display:flex;align-items:center;gap:6px}
.ico{width:8px;height:8px;border:1.2px solid var(--grey);border-radius:2px;flex:none}

.testi{height:181px;background:radial-gradient(ellipse at 30% 50%,#6a6a6a,#3a3a3a 70%);color:var(--white);text-align:center}
.testi .h2{left:0;width:100%;top:30px;font-size:11.5px;color:var(--white)}
.qmark{left:0;width:100%;top:62px;font-size:26px;font-weight:700;line-height:26px;font-family:Georgia,serif;color:var(--white)}
.testi .copy{left:60px;width:352px;top:94px;font-size:6px;line-height:9px}
.dots{display:flex;gap:4px;justify-content:center}
.dots i{width:4px;height:4px;border-radius:50%;background:#999;display:block}
.dots i:first-child{background:var(--gold)}
.testi .dots{left:0;width:100%;top:145px}

.news{height:251px;background:var(--white)}
.news .h2{left:0;width:100%;text-align:center;top:34px;font-size:12px}
.cards{left:29px;top:57px;display:flex;gap:12px}
.card{width:123px;height:180px;background:var(--white);box-shadow:0 1px 5px rgba(0,0,0,.14);position:relative}
.card .img{height:90px;background:linear-gradient(135deg,#ececec,#b9b9b9)}
.card .t{margin:5px 6px 0;font-size:5.5px;font-weight:600;line-height:7.5px;height:16px}
.card .m{margin:3px 6px 0;font-size:3.8px;color:var(--grey)}
.card .x{margin:5px 6px 0;font-size:4.3px;line-height:6.5px;color:var(--grey)}
.card .f{position:absolute;left:6px;right:6px;bottom:6px;display:flex;justify-content:space-between;font-size:4.5px;color:var(--ink)}

.work{height:246px;background:var(--white)}
.work .h2{left:29px;top:64px;font-size:13px}
.field{position:absolute;border:1px solid var(--line);background:var(--white);font-size:4.5px;color:var(--grey);padding:3px 4px}
.work .submit{left:29px;top:183px;width:74px;height:13px;font-size:5px;color:var(--white)}
.work .work-photo{left:216px;top:22px;width:256px;height:224px;background:linear-gradient(120deg,#e9e5df 0%,#a9b6c8 45%,#2e3138 100%)}

.foot{height:232px;background:var(--panel)}
.foot .brand{left:29px;top:26px;font-size:12px}
.foot .about-t{left:29px;top:52px;width:134px;font-size:4.4px;line-height:7px;color:var(--grey)}
.col-h{font-size:6px;font-weight:500;color:var(--ink)}
.col{font-size:4.2px;line-height:8px;color:var(--grey)}
.reach{left:181px;top:32px}
.reach .row{display:flex;gap:6px;align-items:flex-start;margin-top:6px}
.pin{width:5px;height:5px;border-radius:50% 50% 50% 0;background:var(--gold);transform:rotate(-45deg);flex:none;margin-top:1px}
.sq{width:5px;height:5px;background:var(--gold);flex:none;margin-top:1px;border-radius:1px}
.quick{left:303px;top:32px}
.res{left:379px;top:32px}
.badges{left:372px;top:152px;display:flex;gap:12px}
.badge{width:20px;height:31px;background:#c9262d;border-radius:2px}
.socials{left:29px;top:163px;display:flex;gap:3px}
.socials i{display:block;width:11px;height:11px;border:1.3px solid var(--ink);border-radius:50%}
.legal{left:261px;top:165px;font-size:4px;color:var(--grey)}
.copyr{left:0;width:100%;text-align:center;top:205px;font-size:4px;color:var(--ink)}

/* mobile page */
.mob{position:absolute;left:887px;top:762px;width:152px;height:3331px;background:var(--white);box-shadow:0 0 0 2px #222, 0 2px 10px rgba(0,0,0,.2);border-radius:8px 8px 0 0;overflow:hidden}
.m-head{height:214px;background:var(--panel);position:relative}
.m-head .brand{left:9px;top:30px;font-size:11px}
.m-head .login{left:100px;top:34px;width:46px;height:16px;font-size:6px}
.m-head .kicker{left:9px;top:89px;font-size:7px;color:var(--grey)}
.m-head .sub-kicker{left:9px;top:104px;font-size:10.5px;font-weight:600;letter-spacing:.8px;color:var(--grey)}
.m-head .title{left:9px;top:121px;font-size:22px;line-height:26px;font-weight:600}
.m-head .quote-btn{left:9px;top:187px;width:84px;height:20px;font-size:6px}
.m-hero{height:208px;background:radial-gradient(ellipse at 50% 45%,#d2a283,#b0805f 40%,#ece8e2 85%)}
.m-about{height:363px;position:relative;background:linear-gradient(180deg,#f4f4f3,#ebebea)}
.m-about .video{left:9px;top:9px;width:134px;height:95px;background:linear-gradient(135deg,#f6f6f6,#d6d6d6)}
.m-about .h2{left:9px;top:117px;font-size:14px}
.m-about .copy{left:9px;top:139px;width:134px;font-size:5.8px;line-height:9.8px;color:var(--grey)}
.m-about .more{left:9px;top:325px;width:84px;height:18px;font-size:6px}
.m-why-photo{height:225px;background:linear-gradient(120deg,#e8d4bd,#c99a78 45%,#f1ebe3)}
.m-why{height:337px;position:relative;background:var(--white)}
.m-why .h2{left:9px;top:8px;font-size:15px;line-height:19px}
.m-why ul{left:9px;top:52px;list-style:none;font-size:6.2px;line-height:9px;color:var(--ink)}
.m-why li{display:flex;gap:8px;align-items:flex-start;margin-bottom:11px}
.m-why .ico{width:10px;height:10px}
.m-testi{height:415px;position:relative;background:radial-gradient(ellipse at 40% 40%,#5e5e5e,#333 75%);color:var(--white);text-align:center}
.m-testi .h2{left:0;width:100%;top:27px;font-size:14.5px;color:var(--white)}
.m-testi .qmark{top:60px;font-size:32px}
.m-testi .copy{left:14px;width:124px;top:96px;font-size:7.5px;line-height:11.9px;font-style:italic}
.m-testi .dots{left:0;width:100%;top:390px}
.m-news{height:346px;position:relative;background:var(--white)}
.m-news .h2{left:0;width:100%;text-align:center;top:16px;font-size:15px}
.m-news .card{position:absolute;left:5px;top:43px;width:142px;height:276px}
.m-news .card .img{height:118px}
.m-news .card .t{font-size:7px;line-height:10px;height:22px;margin-top:8px}
.m-news .card .m{font-size:5px;line-height:8px}
.m-news .card .x{font-size:5.6px;line-height:9px}
.m-news .card .f{font-size:5.8px}
.m-news .dots{left:0;width:100%;top:329px}
.m-work-photo{height:173px;background:linear-gradient(120deg,#ebe7e1,#a9b6c8 50%,#2e3138)}
.m-work{height:268px;position:relative;background:var(--white)}
.m-work .h2{left:9px;top:14px;font-size:15px;line-height:19px}
.m-work .field{left:9px;width:134px;font-size:5.5px}
.m-work .submit{left:9px;top:226px;width:104px;height:18px;font-size:6px;color:var(--white)}
.m-foot{height:782px;position:relative;background:var(--panel)}
.m-foot .brand{left:9px;top:17px;font-size:14px}
.m-foot .about-t{left:9px;top:64px;width:136px;font-size:5.8px;line-height:9.6px;color:var(--grey)}
.m-foot .col-h{font-size:7.8px}
.m-foot .col{font-size:5.6px;line-height:10px}
.m-foot .reach{left:9px;top:237px}
.m-foot .reach .row{margin-top:8px}
.m-foot .quick{left:9px;top:375px}
.m-foot .res{left:9px;top:472px}
.m-foot .badges{left:9px;top:618px;gap:22px}
.m-foot .badge{width:26px;height:44px}
.m-foot .socials{left:9px;top:686px}
.m-foot .socials i{width:14px;height:14px}
.m-foot .legal{left:9px;top:718px;font-size:5px}
.m-foot .copyr{top:734px;font-size:5.2px;line-height:8px}
</style>
</head>
<body>

<section class="stage">
  <div class="stage-screen">
    <div class="hero-frame sec hero">
      <div class="abs brand"><span>BRELLA</span><span class="dot"></span></div>
      <div class="abs phone"><span class="sq"></span>214-555-0187</div>
      <div class="abs btn login">Log In</div>
      <nav class="abs nav"><span>Home Loans</span><span>Mortgage Resources</span><span>About Us</span><span>Contact Us</span></nav>
      <p class="abs kicker">WE ARE A</p>
      <p class="abs sub-kicker">RESIDENTIAL</p>
      <h1 class="abs title">Mortgage Company</h1>
      <p class="abs lede">A simplified and customized mortgage financing experience</p>
      <div class="abs btn quote-btn">Get A Quote</div>
      <div class="abs note" role="img" aria-label="Handwritten note with arrow reading your path home starts here"></div>
      <div class="photo hero-photo" role="img" aria-label="Smiling family of four reading a tablet together"></div>
    </div>
  </div>
</section>

<h2 class="board-label label-desk">Home Page</h2>
<h2 class="board-label label-mob">Mobile</h2>

<main class="desk">
  <header class="sec hero">
    <div class="abs brand"><span>BRELLA</span><span class="dot"></span></div>
    <div class="abs phone"><span class="sq"></span>214-555-0187</div>
    <div class="abs btn login">Log In</div>
    <nav class="abs nav"><span>Home Loans</span><span>Mortgage Resources</span><span>About Us</span><span>Contact Us</span></nav>
    <p class="abs kicker">WE ARE A</p>
    <p class="abs sub-kicker">RESIDENTIAL</p>
    <h1 class="abs title">Mortgage Company</h1>
    <p class="abs lede">A simplified and customized mortgage financing experience</p>
    <div class="abs btn quote-btn">Get A Quote</div>
    <div class="abs note" role="img" aria-label="Handwritten note with arrow reading your path home starts here"></div>
    <div class="photo hero-photo" role="img" aria-label="Smiling family of four reading a tablet together"></div>
  </header>

  <section class="sec about">
    <div class="abs video" role="img" aria-label="Sketched whiteboard video thumbnail about the mortgage process"><span class="play"></span></div>
    <h2 class="abs h2">About Us</h2>
    <p class="abs copy">Brella Mortgage is founded with passion and the heart of serving. We strive to keep the mortgage experience simple, efficient, and enjoyable for our clients. Brella Mortgage is here to serve you whether you are looking for the best rates in town with a quick and easy closing, or searching for a trustworthy and experienced mortgage loan officer to guide you through your first home purchase.</p>
    <div class="abs btn more">Read More</div>
  </section>

  <section class="sec why">
    <div class="photo why-photo" role="img" aria-label="Mother hugging her young daughter at home"></div>
    <h2 class="abs h2">Why Choose Us</h2>
    <ul class="abs">
      <li><span class="ico"></span>Conventional, FHA, VA, USDA, Jumbo, or Portfolio loans</li>
      <li><span class="ico"></span>Free Pre-Consultation</li>
      <li><span class="ico"></span>First time home buyers</li>
      <li><span class="ico"></span>Experienced buyers and Investors</li>
      <li><span class="ico"></span>Customer Service</li>
      <li><span class="ico"></span>In-House Processing</li>
      <li><span class="ico"></span>Common Sense Underwriting</li>
      <li><span class="ico"></span>Quick Closing - as early as 15 days.</li>
    </ul>
  </section>

  <section class="sec testi">
    <h2 class="abs h2">Testimonial</h2>
    <div class="abs qmark">&ldquo;</div>
    <p class="abs copy">We have worked with Dan Merrow and the Brella Mortgage team several times and every time has been incredibly pleasant! They genuinely care about their clients and communicate very well to make it a smooth process from start to finish. Give them a call if you need to buy a house or refinance your current one!!</p>
    <div class="abs dots"><i></i><i></i><i></i></div>
  </section>

  <section class="sec news">
    <h2 class="abs h2">News</h2>
    <div class="abs cards">
      <article class="card">
        <div class="img" role="img" aria-label="Government building sign with a VA loan note"></div>
        <h3 class="t">3 Benefits to Consider VA Loans</h3>
        <p class="m">By Lena Ortwell • 03 Nov, 2020</p>
        <p class="x">Surprisingly, most veterans we meet assume a VA loan process will be difficult. It is not more …</p>
        <div class="f"><span>Read More ›</span><span>0</span></div>
      </article>
      <article class="card">
        <div class="img" role="img" aria-label="Clock face with words save money"></div>
        <h3 class="t">3 Tips to SAVE Money during COVID-19</h3>
        <p class="m">By Lena Ortwell • 03 Nov, 2020</p>
        <p class="x">While there are challenges during this unprecedented time due to COVID-19, there are …</p>
        <div class="f"><span>Read More ›</span><span>0</span></div>
      </article>
      <article class="card">
        <div class="img" role="img" aria-label="Desk with a forbearance document and pen"></div>
        <h3 class="t">3 Risks considering Mortgage Forbearance</h3>
        <p class="m">By Lena Ortwell • 03 Nov, 2020</p>
        <p class="x">You may be considering mortgage forbearance or financial relief if you have experienced a financial …</p>
        <div class="f"><span>Read More ›</span><span>0</span></div>
      </article>
    </div>
  </section>

  <section class="sec work">
    <h2 class="abs h2">Let's Work Together</h2>
    <div class="field" style="left:29px;top:88px;width:161px;height:17px">Name</div>
    <div class="field" style="left:29px;top:111px;width:78px;height:16px">Email</div>
    <div class="field" style="left:112px;top:111px;width:78px;height:16px">Phone</div>
    <div class="field" style="left:29px;top:132px;width:161px;height:43px">Message</div>
    <div class="abs btn submit">Submit Now</div>
    <div class="photo work-photo" role="img" aria-label="Loan officer meeting with a senior client at a desk"></div>
  </section>

  <footer class="sec foot">
    <div class="abs brand"><span>BRELLA</span><span class="dot"></span></div>
    <p class="abs about-t">Brella Mortgage Inc. is a residential mortgage company. Brella stands for integrity, knowledge of the market and products, outstanding service, and better ways of helping our clients. The company was founded with the core value of giving, honesty, efficiency, humanity, and doing business with integrity.</p>
    <div class="abs reach">
      <h4 class="col-h">How to Reach Us</h4>
      <div class="col">
        <div class="row"><span class="pin"></span><span>4820 Larkspur Avenue, Suite 310<br>Dallas, TX 75201</span></div>
        <div class="row"><span class="sq"></span><span>Fax: 1-888-555-0142</span></div>
        <div class="row"><span class="sq"></span><span>Phone: 214-555-0187</span></div>
        <div class="row"><span class="sq"></span><span>info@brellamortgage.example</span></div>
      </div>
    </div>
    <div class="abs quick">
      <h4 class="col-h">Quick Link</h4>
      <div class="col" style="margin-top:4px">Home Loans<br>Mortgage Resources<br>About Us<br>Contact Us</div>
    </div>
    <div class="abs res">
      <h4 class="col-h">Resources</h4>
      <div class="col" style="margin-top:4px">Buyer Info<br>Seller Info<br>Home Appraisal<br>Home Inspection<br>Loan Checklist<br>Loan Process<br>Loan Programs</div>
    </div>
    <div class="abs socials"><i></i><i></i><i></i></div>
    <p class="abs legal">Legal | Privacy Policy | Site Map</p>
    <div class="abs badges"><span class="badge" role="img" aria-label="Award badge 2017"></span><span class="badge" role="img" aria-label="Award badge 2014"></span></div>
    <p class="abs copyr">Copyright © 2020 Brella. All Rights Reserved</p>
  </footer>
</main>

<main class="mob">
  <header class="m-head">
    <div class="abs brand"><span>BRELLA</span><span class="dot"></span></div>
    <div class="abs btn login">Log In</div>
    <p class="abs kicker">WE ARE A</p>
    <p class="abs sub-kicker">RESIDENTIAL</p>
    <h1 class="abs title">Mortgage<br>Company</h1>
    <div class="abs btn quote-btn">Get A Quote</div>
  </header>
  <div class="m-hero" role="img" aria-label="Smiling family of four reading a tablet together"></div>

  <section class="m-about">
    <div class="abs video" role="img" aria-label="Sketched whiteboard video thumbnail about the mortgage process"><span class="play"></span></div>
    <h2 class="abs h2">About Us</h2>
    <p class="abs copy">Brella Mortgage is founded with passion and the heart of serving. We strive to keep the mortgage experience simple, efficient, and enjoyable for our clients. Brella Mortgage is here to serve you whether you are looking for the best rates in town with a quick and easy closing, or searching for a trustworthy and experienced mortgage loan officer to guide you through your first home purchase.</p>
    <div class="abs btn more">Read More</div>
  </section>

  <div class="m-why-photo" role="img" aria-label="Mother hugging her young daughter at home"></div>
  <section class="m-why">
    <h2 class="abs h2">Why Choose<br>Us</h2>
    <ul class="abs">
      <li><span class="ico"></span><span>Conventional, FHA, VA,<br>USDA, Jumbo, or<br>Portfolio loans</span></li>
      <li><span class="ico"></span><span>Free Pre-Consultation</span></li>
      <li><span class="ico"></span><span>First time home buyers</span></li>
      <li><span class="ico"></span><span>Experienced buyers and<br>Investors</span></li>
      <li><span class="ico"></span><span>Customer Service<br>In-House Processing</span></li>
      <li><span class="ico"></span><span>Common Sense<br>Underwriting</span></li>
      <li><span class="ico"></span><span>Quick Closing - as<br>early as 15 days.</span></li>
    </ul>
  </section>

  <section class="m-testi">
    <h2 class="abs h2">Testimonial</h2>
    <div class="abs qmark">&ldquo;</div>
    <p class="abs copy">We have worked with Dan Merrow and the Brella Mortgage team several times and every time has been incredibly pleasant! They genuinely care about their clients and communicate very well to make it a smooth process from start to finish. Give them a call if you need to buy a house or refinance your current one!!</p>
    <div class="abs dots"><i></i><i></i><i></i></div>
  </section>

  <section class="m-news">
    <h2 class="abs h2">News</h2>
    <article class="card">
      <div class="img" role="img" aria-label="Government building sign with a VA loan note"></div>
      <h3 class="t">3 Benefits to Consider VA Loans</h3>
      <p class="m">By Lena Ortwell •<br>03 Nov, 2020</p>
      <p class="x">Surprisingly, most veterans we meet assume a VA loan process will be difficult. It is not more …</p>
      <div class="f"><span>Read More ›</span><span>0</span></div>
    </article>
    <div class="abs dots"><i></i><i></i><i></i></div>
  </section>

  <div class="m-work-photo" role="img" aria-label="Loan officer meeting with a senior client at a desk"></div>
  <section class="m-work">
    <h2 class="abs h2">Let's Work<br>Together</h2>
    <div class="field" style="top:58px;height:18px">Name</div>
    <div class="field" style="top:86px;height:18px">Email</div>
    <div class="field" style="top:115px;height:18px">Phone</div>
    <div class="field" style="top:143px;height:62px">Message</div>
    <div class="abs btn submit">Submit Now</div>
  </section>

  <footer class="m-foot">
    <div class="abs brand"><span>BRELLA</span><span class="dot"></span></div>
    <p class="abs about-t">Brella Mortgage Inc. is a residential mortgage company. Brella stands for integrity, knowledge of the market and products, outstanding service, and better ways of helping our clients. The company was founded with the core value of giving, honesty, efficiency, humanity, and doing business with integrity.</p>
    <div class="abs reach">
      <h4 class="col-h">How to Reach Us</h4>
      <div class="col">
        <div class="row"><span class="pin"></span><span>4820 Larkspur Avenue, Suite<br>310 Dallas, TX 75201</span></div>
        <div class="row"><span class="sq"></span><span>Fax: 1-888-555-0142</span></div>
        <div class="row"><span class="sq"></span><span>Phone: 214-555-0187</span></div>
        <div class="row"><span class="sq"></span><span>info@brellamortgage.example</span></div>
      </div>
    </div>
    <div class="abs quick">
      <h4 class="col-h">Quick Link</h4>
      <div class="col" style="margin-top:8px">Home Loans<br>Mortgage Resources<br>About Us<br>Contact Us</div>
    </div>
    <div class="abs res">
      <h4 class="col-h">Resources</h4>
      <div class="col" style="margin-top:8px">Buyer Info<br>Seller Info<br>Home Appraisal<br>Home Inspection<br>Loan Checklist<br>Loan Process<br>Loan Programs</div>
    </div>
    <div class="abs badges"><span class="badge" role="img" aria-label="Award badge 2017"></span><span class="badge" role="img" aria-label="Award badge 2014"></span></div>
    <div class="abs socials"><i></i><i></i><i></i></div>
    <p class="abs legal">Legal | Privacy Policy | Site Map</p>
    <p class="abs copyr">Copyright © 2020 Brella.<br>All Rights Reserved</p>
  </footer>
</main>

<p class="thanks">Thanks For<br>Watching</p>

</body>
</html>
```